Plump Wally's Terrier Store - balms

We are looking for a logo design for our new Bulldog butter tins and website. Inspired by our little fat bulldog Wally who has very sensitive skin issues we have scoured the earth to find something for him - turns out only the most natural of ingredients suits our boy so we set out to get something made just for him. All natural, all organic and want to share it with other dogs and their mums and dads.

Wally is a red and white bulldog and we really would like a design that is as close to resembling him as possible. See logo image below - but with Wally and smiling! Essential the face markings are captured as much as possible (e.g. the dot on his head, eye patch etc). Options to see either just face or something similar to the pic titled Plump Wally.

Important to convey natural and organic colouring. Organic type symbol.

Classy upmarket look. Eyecatching. Strong branding potential. see the meadow hound works http://meadowhoundworks.example/shop/ as an example of simple but classy.

Logo to include wording Plump Wally, 100% Natural & Organic, Terrier Salve.

Some photos included below of Wally. Can also be seen on instagram @plumpwallytheterrier.

Tin will be similar to surfers wax - Dad is a surfer and so is Wally! Rectangular. Estimated dimensions 110mmx80mmx25mm (see similar image).
Thank you!

Target Market(s)

Pet owners who adore their pet babies!

Industry/Entity Type

Shop

Requirements
Must have
• Be designed for a rectangular tin Estimated dimensions 110mmx80mmx25mm. Landscape view
• Organic logo (see file upload) located in corner.
• Net Wt 50gm
• Classy upmarket look but simple. Eyecatching. Not too cartoonish.
• Logo to include wording Plump Wally, 100% Organic, Skin Balm
• Must capture Wally's facemarkings - dot on head, eye patch, dots around nose and mouth.
• Key colours of Wally (reddy-brown & tan /black and white) - probably don't want too many other colours - keep simple and classy
• Looking for a coloured background for the label - potentially same colour as Wally to give a kind of a natural feel.
Should not have
• design for a round tin

```html
<!DOCTYPE html>
<html lang="en">
<head>
<meta charset="utf-8">
<title>Plump Wally's Terrier Store – Dog Balm Tin Label</title>
<link href="https://fonts.googleapis.com/css2?family=Gochi+Hand&family=Raleway:wght@700;800&display=swap" rel="stylesheet">
<style>
  :root {
    --page: #ffffff;
    --edge: #c9c9c9;
    --bark: #6b4022;
    --leaf: #6fa534;
    --linen: #e4dacb;
    --linen-light: #efe8dc;
    --rust: #8f3a12;
    --cream: #ffffff;
  }
  * { box-sizing: border-box; margin: 0; padding: 0; }
  html, body {
    width: 1200px; height: 876px; overflow: hidden;
    background: var(--page);
  }
  .canvas {
    position: relative; width: 1200px; height: 876px;
    background: var(--page);
  }
  .trim-line {
    position: absolute; left: 5px; top: 5px; right: 5px; bottom: 5px;
    border: 1px solid var(--edge);
  }
  .label-frame {
    position: absolute; left: 40px; top: 38px; width: 1120px; height: 800px;
    background: var(--bark); border-radius: 72px;
  }
  .label-border {
    position: absolute; left: 68px; top: 66px; width: 1064px; height: 744px;
    background: var(--leaf); border-radius: 50px;
  }
  .label-field {
    position: absolute; left: 86px; top: 84px; width: 1028px; height: 708px;
    border-radius: 34px;
    background: radial-gradient(ellipse at 50% 45%, var(--linen-light), var(--linen) 75%);
  }
  .net-weight {
    position: absolute; left: 68px; top: 66px; width: 178px; height: 86px;
    background: var(--leaf);
    border-radius: 50px 0 40px 0;
    display: flex; align-items: center; padding-left: 34px; gap: 6px;
    color: var(--cream); font-family: "Raleway", sans-serif;
  }
  .net-weight__label { font-weight: 800; font-size: 19px; line-height: 17px; }
  .net-weight__value { font-weight: 800; font-size: 40px; letter-spacing: -1px; }
  .mascot-badge {
    position: absolute; left: 365px; top: 20px; width: 470px; height: 470px;
  }
  .brand-name {
    position: absolute; left: 850px; top: 140px; width: 250px;
    text-align: center;
    font-family: "Raleway", sans-serif; font-weight: 800;
    font-size: 48px; line-height: 56px; color: var(--bark);
  }
  .claim {
    position: absolute; left: 0; top: 502px; width: 1200px; text-align: center;
    font-family: "Gochi Hand", cursive; font-size: 64px; color: var(--leaf);
    letter-spacing: 1px;
  }
  .product-name {
    position: absolute; left: 0; top: 570px; width: 1200px; text-align: center;
    font-family: "Gochi Hand", cursive; font-size: 150px; line-height: 150px;
    font-weight: 400; color: var(--bark); letter-spacing: 2px;
  }
  .product-name__accent { color: var(--rust); }
  .usage {
    position: absolute; left: 0; top: 728px; width: 1200px; text-align: center;
    font-family: "Raleway", sans-serif; font-weight: 700; font-size: 29px;
    color: var(--bark);
  }
</style>
</head>
<body>
<main class="canvas">
  <div class="trim-line"></div>
  <div class="label-frame"></div>
  <div class="label-border"></div>
  <div class="label-field"></div>

  <div class="net-weight">
    <span class="net-weight__label">Net<br>Wt.</span>
    <span class="net-weight__value">50g</span>
  </div>

  <svg class="mascot-badge" viewBox="0 0 470 470">
    <defs>
      <radialGradient id="mascot-tone" cx="50%" cy="50%" r="50%">
        <stop offset="0%" stop-color="#ffffff"/>
        <stop offset="60%" stop-color="#f3ece6"/>
        <stop offset="100%" stop-color="#b06a3c"/>
      </radialGradient>
    </defs>
    <circle cx="235" cy="235" r="235" fill="var(--cream)"/>
    <circle cx="235" cy="235" r="222" fill="var(--leaf)"/>
    <circle cx="235" cy="235" r="200" fill="var(--bark)"/>
    <circle cx="235" cy="225" r="172" fill="url(#mascot-tone)"
            role="img" aria-label="Illustrated bulldog head, red and white markings, smiling"/>
  </svg>

  <p class="brand-name">Plump<br>Wally</p>

  <p class="claim">100% NATURAL</p>
  <h1 class="product-name">DOG B<span class="product-name__accent">A</span>LM</h1>
  <p class="usage">for dry and cracked noses, paws, skin</p>
</main>
</body>
</html>
```